Product Label Design

Need a product design for our Epsom salt product, needs to have a luxurious simple feel to it. The picture attached is our brand and wordage on it, the bag we think should be a stand up bag that should be offwhite/creme color. The other picture are products that we like. We updated the packaging to be a Kraft tube box, please see the attached photo for dimensions.

```html
<!DOCTYPE html>
<html lang="en">
<head>
<meta charset="utf-8">
<title>ORA Ascend Epsom Salt Label</title>
<link rel="stylesheet" href="https://fonts.googleapis.com/css2?family=Poppins:wght@400;500;700&display=swap">
<style>
  :root {
    --backdrop: #e6e6e6;
    --paper: #ffffff;
    --ink: #0b0b0b;
    --accent: #29abe2;
  }
  html, body {
    margin: 0;
    padding: 0;
    width: 1200px;
    height: 1091px;
    overflow: hidden;
    background: var(--backdrop);
    font-family: "Poppins", sans-serif;
    color: var(--ink);
  }
  .label {
    position: absolute;
    left: 150px;
    top: 30px;
    width: 901px;
    height: 1031px;
    background: var(--paper);
  }
  .frame {
    position: absolute;
    left: 155px;
    top: 153px;
    width: 632px;
    height: 810px;
    border-left: 2px solid var(--ink);
    border-right: 2px solid var(--ink);
    box-sizing: border-box;
  }
  .frame-cap {
    position: absolute;
    top: 153px;
    height: 2px;
    background: var(--ink);
  }
  .frame-cap--left { left: 155px; width: 65px; }
  .frame-cap--right { left: 721px; width: 66px; }
  .brand-name {
    position: absolute;
    left: 220px;
    width: 501px;
    top: 46px;
    margin: 0;
    text-align: center;
    font-weight: 700;
    font-size: 205px;
    line-height: 1;
    letter-spacing: -0.01em;
    white-space: nowrap;
  }
  .variant {
    position: absolute;
    left: 0;
    width: 100%;
    top: 348px;
    margin: 0;
    text-align: center;
    font-weight: 700;
    font-size: 57px;
    line-height: 1;
    letter-spacing: 0.22em;
    color: var(--accent);
  }
  .descriptor {
    position: absolute;
    left: 0;
    width: 100%;
    top: 406px;
    margin: 0;
    text-align: center;
    font-weight: 500;
    font-size: 21px;
    letter-spacing: 0.15em;
  }
  .divider {
    position: absolute;
    left: 394px;
    top: 452px;
    width: 153px;
    height: 14px;
  }
  .ingredients {
    position: absolute;
    left: 0;
    width: 100%;
    top: 482px;
    margin: 0;
    padding: 0;
    list-style: none;
    text-align: center;
    font-weight: 500;
    font-size: 21px;
    line-height: 27px;
    letter-spacing: 0.1em;
  }
  .scenery {
    position: absolute;
    left: 155px;
    top: 631px;
    width: 632px;
    height: 189px;
    background: var(--ink);
  }
  .weight-band {
    position: absolute;
    left: 155px;
    top: 836px;
    width: 632px;
    height: 127px;
    background: var(--ink);
    color: var(--paper);
    display: flex;
    align-items: center;
    justify-content: center;
    font-weight: 500;
    font-size: 29px;
    letter-spacing: 0.13em;
  }
</style>
</head>
<body>
  <main class="label">
    <div class="frame"></div>
    <div class="frame-cap frame-cap--left"></div>
    <div class="frame-cap frame-cap--right"></div>

    <h1 class="brand-name">ORA</h1>

    <h2 class="variant">ASCEND</h2>
    <p class="descriptor">US SOURCED PURE EPSOM SALT</p>

    <svg class="divider" viewBox="0 0 153 14" aria-hidden="true">
      <path d="M0 7 q4.25 -6 8.5 0 t8.5 0 t8.5 0 t8.5 0 t8.5 0 t8.5 0 t8.5 0 t8.5 0 t8.5 0 t8.5 0 t8.5 0 t8.5 0 t8.5 0 t8.5 0 t8.5 0 t8.5 0 t8.5 0 t8.5 0" fill="none" stroke="#0b0b0b" stroke-width="1.5"/>
    </svg>

    <ul class="ingredients">
      <li>(Magnesium Sulfate)</li>
      <li>+Abies Sibirica</li>
      <li>+Fir Balsam</li>
    </ul>

    <div class="scenery" role="img" aria-label="Black and white illustration of snow-capped mountain peaks"></div>

    <div class="weight-band">NET WT. 3LBS (1360g)</div>
  </main>
</body>
</html>
```